Business Card Design

I need a Business Card that will catch the attention that will not get thrown in a Drawer. I have 23 companies I use for Auto, Home, Life, and Business Insurance. I make sure that people have the best coverage for the $ spent.

Industry/Entity Type

Business

Contact Information for Business Card

Dorlin Insurance Agency, Inc., Marcus Helgren, 4375 West Tamber Lane Larkmoor, Westland 45192 555-281-7496, www.dorlinagency.example, friendbook, LinkUp, Gloople+

```html
<!DOCTYPE html>
<html lang="en">
<head>
<meta charset="utf-8">
<title>Dorlin Insurance Agency – Business Card</title>
<link href="https://fonts.googleapis.com/css2?family=Share+Tech+Mono&display=swap" rel="stylesheet">
<style>
  :root {
    --paper: #ffffff;
    --ink: #111111;
    --brand: #ef8f2a;
    --orange: #f7a65a;
    --orange-soft: #fde6d0;
    --green: #b5d97a;
    --green-faint: #f3f8ee;
    --red: #ee6a66;
  }
  html, body {
    margin: 0;
    padding: 0;
    width: 1200px;
    height: 702px;
    overflow: hidden;
    background: var(--paper);
  }
  .card {
    position: relative;
    width: 1200px;
    height: 702px;
    font-family: "Share Tech Mono", monospace;
    color: var(--ink);
  }
  .agency-name {
    position: absolute;
    left: 439px;
    width: 340px;
    top: 256px;
    text-align: center;
    font-size: 23px;
    color: var(--brand);
    white-space: nowrap;
  }
  .holder-name {
    position: absolute;
    right: 391px;
    top: 321px;
    font-size: 23px;
    letter-spacing: 2px;
  }
  .band {
    position: absolute;
    left: 380px;
    width: 444px;
  }
  .band-address {
    top: 356px;
    height: 54px;
    background: linear-gradient(90deg, var(--paper) 0%, var(--orange-soft) 30%, var(--orange) 85%, var(--orange) 100%);
  }
  .band-phone {
    top: 410px;
    height: 44px;
    background: linear-gradient(90deg, var(--green) 0%, var(--green) 6%, var(--green-faint) 30%, var(--paper) 34%, var(--green-faint) 55%, var(--green-faint) 100%);
  }
  .band-links {
    top: 454px;
    height: 29px;
    background:
      radial-gradient(ellipse 110px 22px at 263px 50%, var(--red) 0%, rgba(238,106,102,0.55) 45%, rgba(238,106,102,0) 100%),
      var(--green-faint);
  }
  .address {
    position: absolute;
    left: 413px;
    top: 362px;
    font-size: 14px;
    line-height: 19px;
    letter-spacing: 1px;
  }
  .phone {
    position: absolute;
    left: 588px;
    top: 423px;
    font-size: 16px;
    letter-spacing: 1.5px;
  }
  .links {
    position: absolute;
    left: 414px;
    top: 460px;
    font-size: 12px;
    letter-spacing: 0.8px;
    white-space: nowrap;
  }
</style>
</head>
<body>
  <main class="card">
    <div class="agency-name">Dorlin Insurance Agency, Inc.</div>
    <div class="holder-name">Marcus Helgren</div>

    <div class="band band-address"></div>
    <div class="band band-phone"></div>
    <div class="band band-links"></div>

    <div class="address">4375 West Tamber Lane,<br>Larkmoor, Westland</div>
    <div class="phone">45192 555-281-7496</div>
    <div class="links">www.dorlinagency.example friendbook, LinkUp, Gloople+</div>
  </main>
</body>
</html>
```